Business Cards

Need a neat design for a new business card

Industry/Entity Type

Residential Construction

Contact Information for Business Card

Company Name- KORV Construction Inc.
Owner- Daniel Pruitt
Phone number- (555)270-4418
Email- korvcobuilds@mailbox-example.com
Facebook- www.socialpage-example.com/korvcobuilds

Colors
fefdec

```html
<!DOCTYPE html>
<html lang="en">
<head>
<meta charset="utf-8">
<title>KORV Construction – Business Cards</title>
<link href="https://fonts.googleapis.com/css2?family=Arimo:wght@400;700&display=swap" rel="stylesheet">
<style>
  :root {
    --backdrop: #1c1c1c;
    --card: #050505;
    --ink: #fefdec;
    --rule: #5a5a5a;
  }
  html, body {
    margin: 0;
    padding: 0;
    width: 1200px;
    height: 1015px;
    overflow: hidden;
    background: var(--backdrop);
  }
  .canvas {
    position: relative;
    width: 1200px;
    height: 1015px;
    background: radial-gradient(ellipse at 50% 40%, #2a2a2a 0%, var(--backdrop) 70%);
    font-family: "Arimo", Arial, sans-serif;
    color: var(--ink);
  }
  .card {
    position: absolute;
    width: 620px;
    height: 354px;
    background: var(--card);
    box-shadow: 0 18px 40px rgba(0,0,0,0.6);
  }
  .card-front { left: 110px; top: 95px; }
  .card-back  { left: 470px; top: 545px; }
  .card-frame {
    position: absolute;
    inset: 22px;
    border: 3px solid var(--ink);
  }
  .brand {
    position: absolute;
    display: flex;
    align-items: center;
    font-weight: 400;
    color: var(--ink);
    text-transform: uppercase;
    white-space: nowrap;
  }
  .brand-mark {
    background: var(--ink);
    flex: none;
  }
  .card-front .brand {
    left: 0; right: 0; top: 0; bottom: 0;
    justify-content: center;
    gap: 12px;
    font-size: 30px;
    letter-spacing: 0.06em;
  }
  .card-front .brand-mark { width: 14px; height: 14px; }
  .card-back .brand {
    left: 40px;
    width: 250px;
    top: 165px;
    gap: 8px;
    font-size: 14px;
    letter-spacing: 0.04em;
  }
  .card-back .brand-mark { width: 10px; height: 10px; }
  .divider {
    position: absolute;
    left: 300px;
    top: 105px;
    width: 1px;
    height: 150px;
    background: var(--rule);
  }
  .contact {
    position: absolute;
    left: 320px;
    top: 110px;
    right: 26px;
  }
  .contact-name {
    margin: 0;
    font-size: 19px;
    font-weight: 700;
    letter-spacing: 0.01em;
    text-transform: uppercase;
  }
  .contact-role {
    margin: 2px 0 22px 8px;
    font-size: 14px;
  }
  .contact-list {
    list-style: none;
    margin: 0;
    padding: 0;
  }
  .contact-list li {
    display: flex;
    align-items: center;
    gap: 7px;
    font-size: 12.5px;
    line-height: 20px;
    white-space: nowrap;
  }
  .contact-list svg { width: 12px; height: 12px; flex: none; }
  .dot {
    width: 8px; height: 8px; margin: 0 2px;
    border-radius: 50%;
    background: var(--ink);
    flex: none;
  }
</style>
</head>
<body>
<div class="canvas">

  <section class="card card-front">
    <div class="card-frame"></div>
    <div class="brand"><span class="brand-mark"></span>KORV Construction Inc.</div>
  </section>

  <section class="card card-back">
    <div class="card-frame"></div>
    <div class="brand"><span class="brand-mark"></span>KORV Construction Inc.</div>
    <div class="divider"></div>
    <div class="contact">
      <p class="contact-name">Daniel Pruitt</p>
      <p class="contact-role">Owner</p>
      <ul class="contact-list">
        <li>
          <svg viewBox="0 0 24 24" aria-hidden="true"><path fill="#fefdec" d="M6.6 10.8a15.1 15.1 0 0 0 6.6 6.6l2.2-2.2a1 1 0 0 1 1-.25 11.4 11.4 0 0 0 3.6.57 1 1 0 0 1 1 1V20a1 1 0 0 1-1 1A17 17 0 0 1 3 4a1 1 0 0 1 1-1h3.5a1 1 0 0 1 1 1c0 1.250.2 2.45.57 3.57a1 1 0 0 1-.25 1z"/></svg>
          (555)270-4418
        </li>
        <li>
          <svg viewBox="0 0 24 24" aria-hidden="true"><rect x="2" y="5" width="20" height="14" fill="none" stroke="#fefdec" stroke-width="2"/><path d="M2 5l10 8 10-8" fill="none" stroke="#fefdec" stroke-width="2"/></svg>
          korvcobuilds@mailbox-example.com
        </li>
        <li>
          <span class="dot"></span>
          www.socialpage-example.com/korvcobuilds
        </li>
      </ul>
    </div>
  </section>

</div>
</body>
</html>
```